Redesign Charity Golf Outing Flyer

We need a redesign of our current golf outing flyer. The charity is in the name of a fallen police officer and the funds help scholarships for future police officers and community projects. I have included the artwork from last year. We brand everything with "The Chief 417" because Derek's badge number was 417 and he often told people he was "THE CHIEF". The details on the flyer will need to be editable (we have access to the full Adobe creative suite). While the cause is serious the event itself is fun so feel free to have fun with it.

Target Market(s)

Golfers and people who want to donate.

Industry/Entity Type

Charity

Font styles to use
Sans Serif

Colors
0555a3

Requirements
Must have
• All information included on last years flyer.
Nice to have
• A modern feel.
Should not have
• N/a

```html
<!DOCTYPE html>
<html lang="en">
<head>
<meta charset="utf-8">
<title>Giving on the Green – Charity Golf Outing</title>
<link href="https://fonts.googleapis.com/css2?family=Cabin:ital,wght@0,400;0,600;0,700;1,400;1,600&family=Didact+Gothic&display=swap" rel="stylesheet">
<style>
  :root{
    --green:#17663a;
    --green-dark:#0f5a30;
    --turf-1:#2f5a1c;
    --turf-2:#6f9a2e;
    --turf-3:#9cc23c;
    --gold-1:#b8893a;
    --gold-2:#e8c98a;
    --maroon:#7a1f1a;
    --ink:#1d1d1d;
    --grey-text:#666;
    --panel:#e3e3e3;
    --white:#fff;
  }
  *{margin:0;padding:0;box-sizing:border-box}
  html,body{width:848px;height:1200px;overflow:hidden;background:#fff}
  body{font-family:'Cabin',sans-serif;color:var(--ink)}
  .flyer{position:relative;width:848px;height:1200px;overflow:hidden;background:#fff}
  .abs{position:absolute}

  .hero-photo{left:0;top:0;width:848px;height:496px;
    background:radial-gradient(ellipse at 70% 20%,#e9efe6 0,#c9d8b8 14%,transparent 30%),
      linear-gradient(180deg,var(--turf-1) 0%,#3f6d22 35%,var(--turf-2) 62%,var(--turf-3) 80%,#5e8c26 100%)}

  .event-name{left:64px;top:78px;width:310px;color:var(--white);font-family:'Didact Gothic',sans-serif;font-size:24px;line-height:1.3;text-align:center}
  .event-name .mark{display:block;width:64px;height:64px;border-radius:50%;background:var(--white);margin:0 auto 14px;opacity:.95}

  .headline{left:32px;top:322px;color:var(--white);font-family:'Didact Gothic',sans-serif;font-size:45px;letter-spacing:.5px}
  .tagline{left:32px;top:382px;color:var(--white);font-weight:600;font-size:19px;line-height:26px}

  .details-bg{left:0;top:496px;width:848px;height:312px;background:linear-gradient(180deg,#fff 0%,#f3f3f3 60%,#e6e6e6 100%)}

  .portrait{left:422px;top:402px;width:182px;height:182px;border-radius:50%;border:5px solid #fff;box-shadow:0 0 0 1px #bbb;
    background:radial-gradient(circle at 50% 40%,#e7d9cf 0,#d6c2b4 28%,#bfbfbf 45%,#f2f2f2 60%),#eee}
  .memorial-band{left:608px;top:446px;width:240px;height:118px;background:linear-gradient(100deg,var(--gold-1),var(--gold-2) 70%,#f3e3bd)}
  .memorial-band p{position:absolute;left:26px}
  .memorial-band .lead{top:8px;color:#fff;font-family:'Didact Gothic',sans-serif;font-size:25px}
  .memorial-band .nick{top:38px;color:#fff;font-weight:700;font-size:30px;letter-spacing:.5px}
  .memorial-band .name{top:80px;color:var(--maroon);font-size:23px}

  .scramble-title{left:32px;top:504px;color:var(--green);font-weight:700;font-size:35px}
  .rule{height:1.5px;background:var(--green)}
  .date{left:36px;top:558px;font-weight:600;font-size:26px}
  .time{left:36px;font-size:21px;color:var(--green);font-weight:700}
  .time .hr{font-family:'Didact Gothic',sans-serif;font-weight:400}
  .note{left:155px;top:630px;color:var(--green);font-style:italic;font-size:14px}

  .venue{left:32px;top:714px}
  .venue h3{font-size:21px;font-weight:700}
  .venue p{font-family:'Didact Gothic',sans-serif;font-size:17px;line-height:26px}

  .fee{left:600px;top:574px;width:218px;text-align:center}
  .fee h4{font-size:21px;font-weight:600}
  .price{position:absolute;top:34px;width:96px;text-align:center}
  .price .amt{font-weight:700;font-size:38px;border-bottom:1.5px solid #999;padding-bottom:2px}
  .price .amt small{font-size:20px;font-weight:400}
  .price .lbl{font-family:'Didact Gothic',sans-serif;font-size:21px}
  .fee .divider{position:absolute;left:105px;top:54px;width:1.5px;height:44px;background:#888}
  .includes{left:600px;top:690px;width:218px;text-align:center;color:var(--grey-text);font-weight:600;font-size:15px;line-height:21px}

  .register{left:508px;top:738px;width:340px;height:70px;background:var(--green);border-top-left-radius:24px;color:#fff;text-align:center;padding-top:10px;font-size:18px;line-height:30px}
  .register .url{font-weight:700;font-size:19px}

  .shadow-line{left:0;top:806px;width:508px;height:4px;background:linear-gradient(90deg,#999,#333 60%,#555)}

  .captain{left:30px;top:822px;width:458px}
  .captain h3{font-weight:700;font-size:19px;margin-bottom:6px}
  .field{display:flex;align-items:flex-end;font-family:'Didact Gothic',sans-serif;font-size:15px;height:32px}
  .field .dots{flex:1;border-bottom:1.5px dotted #555;margin:0 4px 5px}
  .field .dots.short{flex:0 0 215px}

  .mail-in{left:0;top:1114px;width:508px;height:86px;background:var(--green);color:#fff;padding:6px 0 0 30px}
  .mail-in .deadline{font-size:20px}
  .mail-in .deadline b{font-weight:700}
  .mail-in .inst{font-size:14px;margin-top:2px}
  .mail-in .payee{font-size:16px;font-style:italic;font-weight:600;margin-top:2px}

  .sponsor-panel{left:508px;top:810px;width:340px;height:390px;background:var(--panel)}
  .sponsor{left:524px;top:826px;width:306px}
  .sponsor .ask{font-weight:700;font-size:19px}
  .sponsor .big{font-family:'Didact Gothic',sans-serif;font-size:29px;margin-top:-2px}
  .sponsor .label{font-size:19px;margin-top:18px}
  .sponsor .hint{font-size:11px}
  .sponsor .line{border-bottom:1.5px dotted #555;margin-top:26px}
  .sponsor .line.short{width:190px;margin-top:30px}

  .contact{left:544px;top:1066px;width:276px;height:134px;background:#fff;padding:10px 0 0 28px;font-size:17px;line-height:25px}
  .contact .q{font-family:'Didact Gothic',sans-serif}
  .contact .who{font-weight:700;font-size:19px}
</style>
</head>
<body>
<div class="flyer">
  <div class="abs hero-photo" role="img" aria-label="Close-up photo of a gloved hand placing a golf ball on a tee over green grass"></div>

  <div class="abs event-name">
    <span class="mark"></span>
    3rd Annual Derek D. Harlan Memorial &amp; Scholarship
  </div>

  <h1 class="abs headline">Giving on the Green:</h1>
  <p class="abs tagline">A Charity Golf Outing for “THE CHIEF 417”<br>Benefiting future police officers and<br>community projects</p>

  <div class="abs details-bg"></div>

  <div class="abs memorial-band">
    <p class="lead">Remembering</p>
    <p class="nick">“THE CHIEF”</p>
    <p class="name">Derek D. Harlan</p>
  </div>
  <div class="abs portrait" role="img" aria-label="Portrait photo of Officer Derek D. Harlan in uniform"></div>

  <h2 class="abs scramble-title">Golf Scramble</h2>
  <div class="abs rule" style="left:32px;top:554px;width:356px"></div>
  <p class="abs date">Saturday-August 00, 2016</p>
  <div class="abs rule" style="left:32px;top:592px;width:356px"></div>
  <p class="abs time" style="top:600px">09.00<span class="hr">AM - </span>Registration</p>
  <p class="abs note">(Day of scramble registrations are welcome)</p>
  <p class="abs time" style="top:658px">10.00<span class="hr">AM - </span>Shotgun Start</p>

  <div class="abs venue">
    <h3>Cedar Ridge Golf Course</h3>
    <p>1450 Willow Bend Rd., Ashford, OH 44900</p>
    <p>Ph : (419) 555-0142</p>
  </div>

  <div class="abs fee">
    <h4>Entry Fee :</h4>
    <div class="price" style="left:0"><div class="amt"><small>$</small>55</div><div class="lbl">Person</div></div>
    <div class="divider"></div>
    <div class="price" style="left:118px"><div class="amt"><small>$</small>220</div><div class="lbl">Team</div></div>
  </div>
  <p class="abs includes">Includes: Green Fees,<br>cart and dinner</p>

  <div class="abs register">
    <div><b>Register</b> below or online at:</div>
    <div class="url">www.417golf.eventpage.com</div>
  </div>

  <div class="abs shadow-line"></div>

  <div class="abs captain">
    <h3>Team Captain Information:</h3>
    <div class="field">Captain’s Name:<span class="dots"></span></div>
    <div class="field">Address:<span class="dots"></span></div>
    <div class="field">City:<span class="dots"></span>State:<span class="dots"></span>Zip:<span class="dots"></span></div>
    <div class="field">Captain’s Phone:<span class="dots short"></span></div>
    <div class="field">Captain’s Mail:<span class="dots"></span></div>
    <div class="field">Player#2 Name:<span class="dots"></span></div>
    <div class="field">Player#3 Name:<span class="dots"></span></div>
    <div class="field">Player#4 Name:<span class="dots"></span></div>
  </div>

  <div class="abs mail-in">
    <p class="deadline">Mail-in Deadline: <b>August 1, 2016</b></p>
    <p class="inst">Mail this completed form with check(s) made payable to :</p>
    <p class="payee">“The Officer Derek D. Harlan Memorial Scholarship Fund”</p>
  </div>

  <div class="abs sponsor-panel"></div>
  <div class="abs sponsor">
    <p class="ask">Can’t Make it or Don’t Golf?</p>
    <p class="big">Sponsor a hole/tee:</p>
    <p class="label">Name/Business</p>
    <p class="hint">(Attach business card if possible):</p>
    <div class="line"></div>
    <p class="label">Donation Amount:</p>
    <div class="line short"></div>
  </div>

  <div class="abs contact">
    <p class="q">Any Questions Contact:</p>
    <p class="who">Dale Morton</p>
    <p>820 Maple Hollow Lane</p>
    <p>Fairview, OH 44908</p>
    <p>(419) 555-0187</p>
  </div>
</div>
</body>
</html>
```